Property Investment eBook Cover

I am a long established Australian property investment adviser, analyst and consultant who is now in semi-retired mode and have re-branded to reflect a more casual and personal approach to advising my property investor clients. I am writing a 'revised edition' to a book written in partnership with my father 20 years ago and need an eBook Cover for this new edition. The eBook will be uploaded to all the regular Australian providers (Larkfield Reader, Quince Folio, Tavi, Pagemarten)

The 3 key elements in the book cover are:

Title: The Harvest Engine of Land. The word 'Property' should be larger and more prominent. eg "The Wealth Power of" could be 1/3 the size of "Property" - with both justified left

Edition: Sydney 2021. "Sydney 2021" should be the focus and dominant imagery of the eBook cover and more prominent than the Title or Author

Author: Colin Marsh, The Housing Ledger Guide. The word "Author" should not appear. "The Housing Ledger Guide" should appear underneath Colin Marsh and justified to Colin Marsh, therefore a smaller font.

The cover should be simple, but eye-catching. No property images, more of an abstract background, than a background with an image. Our preferred colour palette is more blues/greens. Prefer SerifFonts

Copy of book published 20 years ago attached for reference only

```html
<!DOCTYPE html>
<html lang="en">
<head>
<meta charset="utf-8">
<title>The Harvest Engine of Land — Colin Marsh</title>
<link rel="stylesheet" href="https://fonts.googleapis.com/css2?family=Gilda+Display&family=Libre+Baskerville:ital,wght@0,700;1,400&family=Raleway:wght@400;500&display=swap">
<style>
  :root {
    --field-dark: #086a31;
    --field-light: #228a48;
    --panel-green: #02672d;
    --banner-red: #e2001f;
    --stripe-gold: #f7e200;
    --stripe-amber: #d07a10;
    --title-white: #ffffff;
    --title-gold: #dcc200;
  }
  * { margin: 0; padding: 0; box-sizing: border-box; }
  html, body { width: 750px; height: 1200px; overflow: hidden; }
  body {
    position: relative;
    background: radial-gradient(ellipse at 50% 50%, var(--field-light) 0%, var(--field-dark) 75%);
  }
  .cover {
    position: absolute;
    left: 65px; top: 65px;
    width: 619px; height: 1069px;
    background: var(--panel-green);
    box-shadow: 0 0 10px 3px rgba(255,255,255,0.55);
  }
  .cover-art { position: absolute; inset: 0; width: 619px; height: 1069px; overflow: visible; }
  .edition-label { font-family: "Libre Baskerville", Georgia, serif; font-style: italic; font-size: 35px; fill: var(--title-white); }
  .edition-place { font-family: "Libre Baskerville", Georgia, serif; font-weight: 700; font-size: 38px; fill: var(--title-white); }
  .title-small { font-family: "Gilda Display", Georgia, serif; font-style: italic; font-size: 42px; fill: var(--title-white); }
  .title-main { font-family: "Gilda Display", Georgia, serif; font-size: 128px; fill: var(--title-white); }
  .title-key { font-family: "Gilda Display", Georgia, serif; font-size: 370px; fill: var(--title-gold); }
  .title-rule { stroke: var(--title-white); stroke-width: 2; }
  .author {
    position: absolute; left: 0; right: 0; top: 945px;
    text-align: center; color: var(--title-white);
    font-family: "Raleway", Arial, sans-serif;
  }
  .author-name { font-size: 48px; font-weight: 500; line-height: 1; }
  .author-tagline { font-size: 27px; font-weight: 400; margin-top: 14px; }
</style>
</head>
<body>
  <main class="cover">
    <svg class="cover-art" viewBox="0 0 619 1069" xmlns="http://www.w3.org/2000/svg">
      <defs>
        <linearGradient id="stripe" x1="0" y1="1" x2="1" y2="0">
          <stop offset="0" stop-color="var(--stripe-gold)"/>
          <stop offset="0.35" stop-color="var(--stripe-amber)"/>
          <stop offset="1" stop-color="var(--stripe-gold)"/>
        </linearGradient>
      </defs>
      <g class="edition-banner">
        <polygon points="0,76 168,0 543,0 0,252" fill="var(--banner-red)"/>
        <line x1="0" y1="97" x2="212" y2="0" stroke="url(#stripe)" stroke-width="4"/>
        <line x1="0" y1="233" x2="502" y2="0" stroke="url(#stripe)" stroke-width="4"/>
        <text class="edition-label" transform="translate(62,120) rotate(-25)">Edition:</text>
        <text class="edition-place" transform="translate(36,182) rotate(-25)">Sydney 2021</text>
      </g>
      <g class="book-title">
        <text class="title-small" x="100" y="297">The</text>
        <line class="title-rule" x1="166" y1="298" x2="591" y2="298"/>
        <text class="title-main" x="31" y="411" textLength="560" lengthAdjust="spacingAndGlyphs">Harvest Engine</text>
        <line class="title-rule" x1="128" y1="486" x2="292" y2="486"/>
        <text class="title-small" x="289" y="486">of</text>
        <line class="title-rule" x1="308" y1="486" x2="593" y2="486"/>
        <text class="title-key" x="24" y="714" textLength="568" lengthAdjust="spacingAndGlyphs">Land</text>
      </g>
    </svg>
    <div class="author">
      <p class="author-name">Colin Marsh</p>
      <p class="author-tagline">The Housing Ledger Guide</p>
    </div>
  </main>
</body>
</html>
```